Presentation card Venture KELO - Tech Incubator from Perú

We need a Design to promote the incubator of technology Startups.
We are in Perú, we work with a string tech filter and develop enterprenurship competencies in the Startup team.
The card is to facilitators and staff memebers of VentureKELO.
We want a clear, modern, tech and agile Design.

We work to help New enterprises of technology here in Perú, we expect the candidates have a big competencies to Research and develop technological products.

We work using methodologies from QRB, Folmestry, Brakewell and Harrowgate univeesities. Our book base is the disciplina of enterpreneur.

We work events all year using diferent formats: Brightforge, Vorne price, OPRA Model Competition you can use these logros in your Design.

Set the name, role, email, cell phone number, address.

Example:
// Contact info section
Tobías Quiroveda
Swift Modeling Hub Manager
tobias.quiroveda@kelo-example.pe
(511) 999 000 417

// Address info section
VentureKELO
Technology-based business incubator
Av. Los Cedrales 884, Valdora
Lima - Perú
web: venture-kelo-example.org.pe
email: venture@kelo-example.pe
phone number: (511) 3926508 ext. 4418

// (optional)Lema section
Making happy using technology

// Social network section
facebook: venturekelooficial

Target Market(s)

Enterprenurship, CTO, Investors, Companies interested on open innovation services

Industry/Entity Type

Information Technology

Contact Information for Business Card

Name, Role, Email, Cell phone number

Colors

Designer to choose colors to be used in the design.

Requirements
Must have
• Logo forms and colors
Nice to have
• I add pictures of the leaders of incubator
Should not have
• No vertical designs

```html
<!DOCTYPE html>
<html lang="en">
<head>
<meta charset="utf-8">
<title>Venture KELO – Business Card</title>
<link rel="stylesheet" href="https://fonts.googleapis.com/css2?family=Open+Sans:wght@400;700&display=swap">
<style>
  :root {
    --page: #3a3b3e;
    --card-dark: #2b2b2d;
    --card-light: #ffffff;
    --brand-magenta: #b8325a;
    --ink: #262626;
    --ink-light: #d7d7d7;
  }
  * { box-sizing: border-box; margin: 0; padding: 0; }
  html, body {
    width: 1200px;
    height: 1000px;
    overflow: hidden;
    background: var(--page);
    font-family: "Open Sans", Arial, sans-serif;
  }
  .canvas {
    position: relative;
    width: 1200px;
    height: 1000px;
  }
  .card {
    position: absolute;
    left: 220px;
    width: 760px;
    height: 434px;
    border-radius: 4px;
    overflow: hidden;
    box-shadow: 0 10px 30px rgba(0,0,0,0.35);
  }
  .card-back {
    top: 46px;
    background: var(--card-dark);
    display: flex;
    align-items: center;
    justify-content: center;
  }
  .card-front { top: 520px; background: var(--card-dark); }
  .card-front .front-shapes {
    position: absolute;
    inset: 0;
    width: 100%;
    height: 100%;
  }
  .brand {
    display: flex;
    align-items: center;
    gap: 12px;
    font-weight: 700;
    letter-spacing: 0.5px;
  }
  .brand-mark {
    width: 22px;
    height: 22px;
    background: var(--brand-magenta);
  }
  .card-back .brand-name { color: var(--card-light); font-size: 54px; }
  .card-front .brand {
    position: absolute;
    top: 112px;
    right: 70px;
  }
  .card-front .brand-name { color: var(--ink); font-size: 38px; }
  .card-front .brand-mark { width: 18px; height: 18px; }
  .person {
    position: absolute;
    left: 44px;
    top: 250px;
    color: var(--ink);
    font-size: 19px;
    line-height: 1.2;
  }
  .person-name {
    color: var(--brand-magenta);
    font-weight: 700;
    font-size: 24px;
    margin-bottom: 2px;
  }
  .contact {
    position: absolute;
    right: 36px;
    bottom: 30px;
    list-style: none;
    color: var(--ink-light);
    font-size: 18px;
    line-height: 1.4;
    text-align: right;
  }
  .contact li {
    display: flex;
    align-items: center;
    justify-content: flex-end;
    gap: 12px;
  }
  .contact svg { width: 18px; height: 20px; flex: none; }
</style>
</head>
<body>
<main class="canvas">
  <section class="card card-back" aria-label="Business card, back">
    <div class="brand">
      <span class="brand-name">Venture KELO</span>
      <span class="brand-mark"></span>
    </div>
  </section>

  <section class="card card-front" aria-label="Business card, front">
    <svg class="front-shapes" viewBox="0 0 760 434" preserveAspectRatio="none" aria-hidden="true">
      <path d="M0,0 H340 Q110,30 0,240 Z" fill="var(--brand-magenta)"/>
      <path d="M0,240 Q110,30 340,0 H760 V170 Q520,430 260,434 H0 Z" fill="var(--card-light)"/>
    </svg>

    <div class="brand">
      <span class="brand-name">Venture KELO</span>
      <span class="brand-mark"></span>
    </div>

    <div class="person">
      <p class="person-name">Tobías Quiroveda</p>
      <p class="person-role">Senior Software<br>Development Engineer</p>
      <p class="person-country">Peru</p>
    </div>

    <ul class="contact">
      <li>836-000-4172
        <svg viewBox="0 0 18 20" aria-label="phone"><rect x="4" y="1" width="10" height="18" rx="2" fill="none" stroke="var(--ink-light)" stroke-width="2"/><circle cx="9" cy="15.5" r="1.2" fill="var(--ink-light)"/></svg>
      </li>
      <li>tobias@kelo-example.pe
        <svg viewBox="0 0 18 20" aria-label="email"><rect x="1" y="5" width="16" height="11" fill="var(--ink-light)"/><path d="M1,5 L9,11 L17,5" fill="none" stroke="var(--card-dark)" stroke-width="1.5"/></svg>
      </li>
    </ul>
  </section>
</main>
</body>
</html>
```